Workout book cover design: Looking for Simple Classic Cover

I need a book cover design for "The Steady Middle". A book on exercises to strengthen the pelvic floor. Basically it's exercises for your torso and hips. I want something tasteful and classic looking.

I like this book cover design: http://www.pagelorn-books.example/Calm-Starters-Gentle-Routines-Ease-ebook/dp/Q93KX7TM41/ref=sr_1_40?ie=UTF8&qid=2958173306&sr=8-40&keywords=exercise+books

Book Title: The Steady Middle
Description to go under title: I'm working on that now and will have ready by the end of the project. (The hidden world of pelvic floor training. Discover the best exercises for creating a strong core, hips and pelvis today!)

Target Market(s)

Mostly women 35-65 and men 60+

Industry/Entity Type

Health And Wellness

Requirements
Must have
• ebook dementions: 1536 x 2048 I think works for all the online publishing companies
• 8x10 for print
Nice to have
• I like this book cover design: http://www.pagelorn-books.example/Calm-Starters-Gentle-Routines-Ease-ebook/dp/Q93KX7TM41/ref=sr_1_40?ie=UTF8&qid=2958173306&sr=8-40&keywords=exercise+books
• This cover is also ok, but no shiny. http://www.pagelorn-books.example/Bedrock-Renew-The-Climb-Poise/dp/4827305519/ref=sr_1_2?ie=UTF8&qid=2958176642&sr=8-2&keywords=foundation+book
Should not have
• I do not like this cover, it's crowded. http://www.pagelorn-books.example/Gym-Drills-Selfweight-flexing-drills-ebook/dp/Q71RWJZNHE/ref=sr_1_2?ie=UTF8&qid=2958174418&sr=8-2&keywords=workout+books
• I do not want anyone on the cover making eye contact.

```html
<!DOCTYPE html>
<html lang="en">
<head>
<meta charset="utf-8">
<title>The Steady Middle – Book Cover</title>
<link rel="stylesheet" href="https://fonts.googleapis.com/css2?family=Merriweather:wght@700;900&display=swap">
<style>
  :root {
    --page-bg: #ffffff;
    --cover-black: #0c0c0d;
    --figure-blue: #5d7fd0;
    --figure-blue-deep: #34509a;
    --shirt-grey: #8f9296;
    --band-pink: #ec008c;
    --text-white: #ffffff;
  }
  * { margin: 0; padding: 0; box-sizing: border-box; }
  html, body {
    width: 1200px;
    height: 1000px;
    overflow: hidden;
    background: var(--page-bg);
  }
  .canvas {
    position: relative;
    width: 1200px;
    height: 1000px;
  }
  .book-cover {
    position: absolute;
    left: 287px;
    top: 123px;
    width: 570px;
    height: 723px;
    background: var(--cover-black);
    overflow: hidden;
    font-family: "Merriweather", Georgia, serif;
    color: var(--text-white);
  }
  .cover-photo {
    position: absolute;
    inset: 0;
    background:
      radial-gradient(ellipse 46% 34% at 50% 62%, var(--shirt-grey) 0%, rgba(143,146,150,0.55) 55%, rgba(143,146,150,0) 100%),
      radial-gradient(ellipse 62% 70% at 50% 48%, var(--figure-blue) 0%, var(--figure-blue-deep) 55%, rgba(52,80,154,0) 85%),
      linear-gradient(180deg, var(--cover-black) 0%, #111217 60%, var(--cover-black) 100%);
  }
  .tagline-band {
    position: absolute;
    left: 0;
    top: 294px;
    width: 100%;
    height: 125px;
    background: var(--band-pink);
    display: flex;
    align-items: center;
    justify-content: center;
  }
  .tagline {
    font-size: 13.5px;
    font-weight: 900;
    line-height: 19px;
    text-align: center;
    text-transform: uppercase;
    letter-spacing: 0.2px;
    margin-top: -10px;
  }
  .book-title {
    position: absolute;
    left: 0;
    top: 470px;
    width: 100%;
    text-align: center;
    font-size: 58px;
    font-weight: 900;
    line-height: 62px;
    text-transform: uppercase;
    letter-spacing: 0.5px;
  }
  .author-name {
    position: absolute;
    left: 0;
    top: 625px;
    width: 100%;
    text-align: center;
    font-size: 23px;
    font-weight: 900;
    text-transform: uppercase;
    letter-spacing: -0.3px;
    transform: scaleX(0.88);
  }
</style>
</head>
<body>
  <div class="canvas">
    <section class="book-cover">
      <div class="cover-photo" role="img" aria-label="Photograph of a seated woman in a grey tank top, shown from the shoulders down, skin tinted blue against a black background"></div>
      <div class="tagline-band">
        <p class="tagline">The hidden world&nbsp; of pelvic floor training.<br>Discover the best exercises for creating<br>a strong core, hips and pelvis today!</p>
      </div>
      <h1 class="book-title">The Steady<br>Middle</h1>
      <p class="author-name">Author Name</p>
    </section>
  </div>
</body>
</html>
```